Moder Business Card Design for Renewables Business

Need a business card design for my business. We collect & repurpose spent coffee ground from cafes. The cards will be made from recycled paper. Needs to fit our corporate colour scheme of white, green & brown (see logo for colour codes). Eco friendly, modern, intresting & eye catching.
This card needs to convey the message of the business and fit into its mantra of eco-friendly, sustainable etc.

Target Market(s)

Cafe Owners, Coffee Drinkers, Recycling Companies, Farmers

Industry/Entity Type

Recycling

Contact Information for Business Card

Name; Peter Halloran
Phone; 0412 386 527
e-mail; info@lumatrove.com.au
website; www.lumatrove.com.au

Font styles to use
Sans Serif
Script

Colors

Designer to choose colors to be used in the design.

Requirements
Must have
• FRONT;
• Logo, Name (Peter Halloran), phone number, e-mail address, website
• BACK;
• On the back in cursive text; 'GOOD THINGS FROM EVERY LAST CUP'
• Small facebook & Instagram logos with text 'Lumatrove'
Should not have
• messy design

```html
<!DOCTYPE html>
<html lang="en">
<head>
<meta charset="utf-8">
<title>Lumatrove Business Card</title>
<link rel="stylesheet" href="https://fonts.googleapis.com/css2?family=Roboto+Condensed:wght@400;700&family=Kaushan+Script&display=swap">
<style>
  :root {
    --canvas: #d9d4cc;
    --kraft: #e6e0d6;
    --charcoal: #2a2927;
    --brown: #6b2f14;
    --green: #6aad3a;
    --green-soft: #7cbf45;
  }
  * { box-sizing: border-box; margin: 0; padding: 0; }
  html, body {
    width: 1200px; height: 848px; overflow: hidden;
    background: var(--canvas);
    font-family: "Roboto Condensed", Arial, sans-serif;
  }
  .stage {
    width: 1200px; height: 848px;
    display: flex; align-items: center; justify-content: center; gap: 40px;
  }
  .card {
    width: 540px; height: 309px; border-radius: 24px;
    display: flex; flex-direction: column; align-items: center;
    box-shadow: 0 6px 18px rgba(0,0,0,.18);
  }
  .brand { display: flex; flex-direction: column; align-items: center; gap: 6px; }
  .brand-dot { border-radius: 50%; border-style: solid; }
  .brand-name { font-weight: 700; letter-spacing: 1.5px; line-height: 1; }

  /* Front */
  .card-front { background: var(--kraft); padding-top: 30px; }
  .card-front .brand-dot { width: 60px; height: 60px; border-width: 4px; border-color: var(--brown); }
  .card-front .brand-name { font-size: 22px; color: var(--green); }
  .person {
    margin-top: 18px; font-weight: 700; font-size: 21px; line-height: 1;
    color: var(--brown); letter-spacing: .5px; text-transform: uppercase;
  }
  .rule { width: 64px; height: 2px; background: var(--brown); margin: 12px 0 14px; }
  .contact-row { display: flex; gap: 22px; font-size: 17px; line-height: 1; color: var(--brown); }
  .contact-item { display: flex; align-items: center; gap: 6px; }
  .contact-item svg { width: 16px; height: 16px; fill: var(--green); }
  .website {
    margin-top: 14px; font-size: 16px; line-height: 1; letter-spacing: 4px; color: var(--green);
  }

  /* Back */
  .card-back { background: var(--charcoal); padding-top: 40px; }
  .card-back .brand { gap: 10px; }
  .card-back .brand-dot { width: 84px; height: 84px; border-width: 5px; border-color: var(--green); }
  .card-back .brand-name { font-size: 32px; color: var(--green-soft); }
  .tagline {
    margin-top: 12px; font-family: "Kaushan Script", cursive;
    font-size: 21px; line-height: 1.2; color: var(--green-soft);
  }
  .social {
    margin-top: 14px; display: flex; align-items: center; gap: 8px;
    font-size: 18px; line-height: 1; color: var(--green-soft);
  }
  .social-mark { width: 16px; height: 16px; background: var(--green-soft); border-radius: 3px; }
</style>
</head>
<body>
<main class="stage">
  <section class="card card-front">
    <div class="brand">
      <span class="brand-dot"></span>
      <span class="brand-name">LUMATROVE</span>
    </div>
    <h1 class="person">Peter Halloran</h1>
    <div class="rule"></div>
    <div class="contact-row">
      <span class="contact-item">
        <svg viewBox="0 0 16 16" aria-hidden="true"><path d="M3 1h3l1.5 4-2 1.2a9 9 0 0 0 4.3 4.3L11 8.5l4 1.5v3a2 2 0 0 1-2 2A12 12 0 0 1 1 3a2 2 0 0 1 2-2z"/></svg>
        0412 386 527
      </span>
      <span class="contact-item">
        <svg viewBox="0 0 16 16" aria-hidden="true"><path d="M1 3h14v10H1z M1 3l7 6 7-6" stroke="#e6e0d6" stroke-width="1.2"/></svg>
        info@lumatrove.com.au
      </span>
    </div>
    <div class="website">www.lumatrove.com.au</div>
  </section>

  <section class="card card-back">
    <div class="brand">
      <span class="brand-dot"></span>
      <span class="brand-name">LUMATROVE</span>
    </div>
    <p class="tagline">Good things from every last cup</p>
    <div class="social">
      <span class="social-mark"></span>
      <span>/Lumatrove</span>
    </div>
  </section>
</main>
</body>
</html>
```